WordPress design project for Verlani Construction

Verlani Construction, Inc. (www.verlaniinc.example) is a private organization. It is run by the same family that founded Verlani Refuse Systems (www.verlani.example), a large, publicly-held waste management organization in the US. While owned by the same family, the two organizations are run independently.
Verlani Construction is a well-established New England USA construction outfit specializing in site development, heavy excavation, aggregate, large-scale/municipal water and sewer systems, and landfill construction and closure. Verlani Construction is not in any way a residential or commercial building contractor.
Verlani Construction also operates hydraulic and hydrostatic service shops, as well as aggregate (gravel, sand, stone, top soil, and anything else aggregate) sites. Both are for more traditional, non-project customers, such as landscapers and other construction companies.
Business contact information is as noted below:
Address:
Verlani Construction, Inc.
48 Quarry Ridge Road
Mendon, Vermont 05829
Telephone:
802-555-0147
Fax:
802-555-0183
Email:
info@verlaniinc.example
A tagline used in a recent advertisement was:
"Committed to providing a complete array of services for over 30 years, we are New England's premier construction company."
In reviewing design ideas internally, we found bits and pieces of the following sites appealing:
RT Construction (Dorwenski) - http://www.rtconstruction.example/
Halbrook Construction - http://www.halbrook.example/
Pelham Construction - http://www.pelhamconstruction.example/
Riverbend Construction Group - http://www.riverbendconstructiongroup.example/
Krage Construction - http://www.krage.example/
Vail Sisters Construction http://www.vailsis.example/
Tolliver Construction http://www.tolliver-corp.example/
The blue in the logo is hex #00253f. The logo was designed by hand many years ago, so the font is unknown.
We would like a fresh, professional design that effectively illustrates what we do in a thoughtful, impressive way.
Target Market(s)
Would-be clients, land developers, waste organizations, energy developers, engineers, surveyors, landscapers, heavy equipment operators and the likes.
Industry/Entity Type
Waste Management
Requirements
Must have
- Lots of media capabilities, such as embedded video (via YouTube is fine), project image gallery, and sliders for various functions.
A large slider on the landing page is critical, as well as space for standard things, such as news/events, job opportunities, project highlights, and the likes.
We also want to highlight things like employee longevity. Some of our team have been with us since the beginning.
We need to add emphasis to the fact that our hydraulic/hydro static services and aggregate operations are for anyone who needs such service or material. Related, we need a place to set prices and descriptions of such material to help site visitors decide what they may need.
We need a place to highlight business partners, such as Amos Fairley and Gruntwell.
We also need form capabilities for things like bid requests and general contacts from the public. Related, there should be social media capabilities.
Nice to have
- This is almost a must have, but we're open to options. The WordPress design should be capable of fitting into the very popular PlumPages Easel theme.

```html
<!DOCTYPE html>
<html lang="en">
<head>
<meta charset="utf-8">
<title>Verlani Construction – Home</title>
<link href="https://fonts.googleapis.com/css2?family=Oswald:wght@300;400;700&display=swap" rel="stylesheet">
<style>
:root{
  --navy:#00253f;
  --nav-active:#0b3266;
  --footer:#0c2c5e;
  --page:#f4f4f4;
  --panel:#e6e6e6;
  --text-grey:#8a8a8a;
  --heading:#1c3d6e;
  --white:#ffffff;
}
*{box-sizing:border-box;margin:0;padding:0}
html,body{width:800px;height:1200px;overflow:hidden;background:var(--page)}
body{font-family:'Oswald',sans-serif;font-weight:300;color:var(--text-grey);position:relative}
.abs{position:absolute}

/* header */
.search{left:549px;top:20px;width:164px;height:17px;background:var(--white);border:1px solid #e4e4e4;font-size:6px;color:#b5b5b5;padding:4px 6px}
.search svg{position:absolute;right:4px;top:3px}
.logo{left:86px;top:46px;display:flex;align-items:center;gap:8px}
.logo-mark{width:16px;height:16px;background:var(--navy)}
.logo-name{font-family:'Oswald',sans-serif;font-weight:700;font-size:30px;color:var(--navy);line-height:1}
.nav{right:87px;top:58px;display:flex;gap:13px;align-items:center}
.nav a{font-size:13px;color:#222;text-decoration:none;line-height:19px}
.nav a.active{background:var(--nav-active);color:var(--white);padding:0 7px}

/* hero */
.hero{left:0;top:117px;width:800px;height:363px;background:linear-gradient(180deg,#6f9ed4 0%,#9cbde0 35%,#c8b8a8 65%,#8a7868 100%)}
.hero-caption{left:0;top:403px;width:800px;height:77px;background:rgba(25,25,25,.78);text-align:center;color:var(--white)}
.hero-caption h1{font-weight:300;font-size:16px;margin-top:8px}
.hero-caption p{font-size:11px;margin-top:1px}
.dots{display:flex;justify-content:center;gap:4px;margin-top:8px}
.dots span{width:9px;height:9px;border-radius:50%;background:var(--white)}
.dots span.on{background:var(--nav-active)}

/* welcome */
.welcome{left:86px;top:506px;width:627px;text-align:center}
.welcome h2{font-weight:300;font-size:13px;color:var(--heading)}
.welcome p{font-size:8.4px;line-height:18.6px;margin-top:9px;letter-spacing:-.1px}

/* columns */
.col-title{font-weight:300;font-size:13px;color:var(--heading);top:628px}
.news-panel{left:86px;top:654px;width:201px;height:252px;background:var(--panel);padding:20px 12px 0 10px}
.news-item{display:flex;gap:10px;margin-bottom:7px}
.thumb{width:51px;height:44px;flex:none}
.news-item p{font-size:8.4px;line-height:13.2px;text-align:justify}
.news-item small{display:block;font-size:7.6px;color:#666;margin-top:5px}
.project-panel{left:299px;top:654px;width:201px;height:125px;background:var(--panel)}
.project-img{position:absolute;left:23px;top:8px;width:153px;height:108px;background:linear-gradient(160deg,#5f95d8,#b2a895 70%,#7b6f5e)}
.chev{position:absolute;top:56px}
.gallery-main{left:513px;top:654px;width:200px;height:125px;background:linear-gradient(180deg,#4d86cf 0%,#8eb6e2 40%,#a39380 75%,#6c5a48 100%)}
.col-text{top:792px;width:201px;font-size:8.4px;line-height:13.3px;text-align:justify}
.thumbs{left:513px;top:837px;display:flex;gap:8px}
.thumbs div{width:62px;height:56px}
.btn{top:910px;height:21px;background:var(--nav-active);color:var(--white);font-size:12px;line-height:21px;padding:0 7px}

/* footer */
.footer{left:0;top:967px;width:800px;height:233px;background:var(--footer);color:var(--white)}
.footer h3{position:absolute;font-weight:300;font-size:12px;top:29px}
.links{position:absolute;top:58px;list-style:none;font-size:9px;line-height:16px}
.news-copy{position:absolute;left:300px;top:56px;width:148px;font-size:8.4px;line-height:14.5px}
.field{position:absolute;left:299px;width:147px;height:18px;background:var(--white);color:#bbb;font-size:8px;padding:3px 9px;border:1px solid #cfd6e0}
.subscribe{position:absolute;left:381px;top:143px;width:65px;height:16px;border-radius:8px;background:#061a36;font-size:9px;text-align:center;line-height:16px}
.social{position:absolute;left:460px;font-size:9px}
.social-dot{position:absolute;left:535px;width:18px;height:18px;border-radius:50%;background:var(--white)}
.partner{position:absolute;left:582px;display:flex;align-items:center;gap:6px;font-size:13px;font-weight:400}
.partner i{display:block;width:14px;height:14px;background:var(--white)}
.copyright{position:absolute;top:196px;width:800px;text-align:center;font-size:8.4px}
</style>
</head>
<body>

<header>
  <div class="abs search">Type search
    <svg width="9" height="9" viewBox="0 0 10 10"><circle cx="4" cy="4" r="3" fill="none" stroke="#999" stroke-width="1.2"/><line x1="6.3" y1="6.3" x2="9" y2="9" stroke="#999" stroke-width="1.4"/></svg>
  </div>
  <div class="abs logo"><span class="logo-mark"></span><span class="logo-name">Verlani</span></div>
  <nav class="abs nav">
    <a class="active" href="#">Home</a><a href="#">About Us</a><a href="#">Services</a><a href="#">Projects</a><a href="#">Partners</a><a href="#">Contact Us</a>
  </nav>
</header>

<section>
  <div class="abs hero" role="img" aria-label="Photo of two business people shaking hands in front of a construction site"></div>
  <div class="abs hero-caption">
    <h1>Committed to providing a complete array of services for over 30 years,</h1>
    <p>we are New England’s premier construction company</p>
    <div class="dots"><span class="on"></span><span></span><span></span><span></span></div>
  </div>
</section>

<section class="abs welcome">
  <h2>Welcome to Verlani Construction Company</h2>
  <p>Lorem Ipsum is simply dummy text of the printing and typesetting industry. Lorem Ipsum has been the industry's standard dummy text ever since the 1500s, when an unknown printer took a galley of type and scrambled it to make a type specimen book. It has survived not only five centuries, but also the leap into electronic typesetting, remaining essentially unchanged. It was popularised in the 1960s with the release of Lettermark sheets containing Lorem Ipsum passages, and more recently with desktop publishing software like Quillbyte PageSetter including versions of Lorem Ipsum.</p>
</section>

<section>
  <h2 class="abs col-title" style="left:86px">Latest News &amp; Events</h2>
  <div class="abs news-panel">
    <div class="news-item"><div class="thumb" role="img" aria-label="Building under construction" style="background:linear-gradient(180deg,#5b8fd0,#8c7a60)"></div>
      <p>Lorem ipsum dolor sit amet, consectetur adipisicing elit, sed do eiusmod tempor incididunt ut labore et dolore magna aliqua.<small>May 2013 ,23rd GST 22.10</small></p></div>
    <div class="news-item"><div class="thumb" role="img" aria-label="City skyline with towers" style="background:linear-gradient(180deg,#4f86cf,#c7a77a)"></div>
      <p>Lorem ipsum dolor sit amet, consectetur adipisicing elit, sed do eiusmod tempor incididunt ut labore et dolore magna aliqua.<small>May 2013 ,23rd GST 22.10</small></p></div>
    <div class="news-item"><div class="thumb" role="img" aria-label="Engineers reviewing plans" style="background:linear-gradient(180deg,#e9e9e9,#6f6f75)"></div>
      <p>Lorem ipsum dolor sit amet, consectetur adipisicing elit, sed do eiusmod tempor incididunt ut labore et dolore magna aliqua.<small>May 2013 ,23rd GST 22.10</small></p></div>
  </div>
  <div class="abs btn" style="left:86px">More News &amp; Events</div>

  <h2 class="abs col-title" style="left:300px">Project Highlights</h2>
  <div class="abs project-panel">
    <div class="project-img" role="img" aria-label="Construction workers in hard hats at a building site"></div>
    <svg class="chev" style="left:10px" width="8" height="14" viewBox="0 0 8 14"><polyline points="7,1 1,7 7,13" fill="none" stroke="#fff" stroke-width="1.5"/></svg>
    <svg class="chev" style="left:183px" width="8" height="14" viewBox="0 0 8 14"><polyline points="1,1 7,7 1,13" fill="none" stroke="#fff" stroke-width="1.5"/></svg>
  </div>
  <p class="abs col-text" style="left:299px">Lorem ipsum dolor sit amet, consectetur adipisicing elit, sed do eiusmod tempor incididunt ut labore et dolore magna aliqua. Ut enim ad minim veniam, quis nostrud exercitation ullamco laboris nisi ut aliquip ex ea commodo consequat. Duis aute irure dolor in reprehenderit in voluptate velit esse cillum dolore eu fugiat nulla pariatur. Excepteur sint occaecat cupidatat non proident, sunt in culpa qui officia deserunt mollit anim id est laborum.</p>
  <div class="abs btn" style="left:299px">Read More</div>

  <h2 class="abs col-title" style="left:514px">Photo gallery</h2>
  <div class="abs gallery-main" role="img" aria-label="Multi-storey building frame with cranes"></div>
  <p class="abs col-text" style="left:513px;width:200px">Lorem ipsum dolor sit amet, consectetur adipisicing elit, sed do eiusmod tempor incididunt ut labore et dolore magna aliqua. Ut enim ad minim veniam, quis nostrud.</p>
  <div class="abs thumbs">
    <div role="img" aria-label="Building site with crane" style="background:linear-gradient(180deg,#4f86cf,#7a6a55)"></div>
    <div role="img" aria-label="Worker on steel structure" style="background:linear-gradient(180deg,#8fb0d8,#a0785a)"></div>
    <div role="img" aria-label="Tower under construction" style="background:linear-gradient(180deg,#3f78c6,#c9a97a)"></div>
  </div>
  <div class="abs btn" style="left:512px">View Photos</div>
</section>

<footer class="abs footer">
  <h3 style="left:87px">Quick Links</h3>
  <ul class="links" style="left:87px"><li>Home</li><li>About Us</li><li>Services</li><li>Projects</li><li>Partners</li><li>Contact Us</li></ul>
  <h3 style="left:194px">Support Links</h3>
  <ul class="links" style="left:193px"><li>Legal Notice</li><li>Privacy Policy</li><li>Terms &amp; Conditions</li><li>Help</li></ul>
  <h3 style="left:300px">Newsletter SignUp</h3>
  <p class="news-copy">Sign-up for our daily emails by entering your information below:</p>
  <div class="field" style="top:90px">Name</div>
  <div class="field" style="top:118px">Enter Your E-Mail ID</div>
  <div class="subscribe">Subscribe</div>
  <h3 style="left:461px">Connect With Us</h3>
  <span class="social" style="top:58px">Chirpline</span><span class="social-dot" style="top:57px"></span>
  <span class="social" style="top:83px">Friendsheet</span><span class="social-dot" style="top:82px"></span>
  <span class="social" style="top:108px">Workwire</span><span class="social-dot" style="top:106px"></span>
  <h3 style="left:565px;top:26px">Business Partners</h3>
  <div class="partner" style="top:100px"><i></i>Amos Fairley</div>
  <div class="partner" style="top:135px"><i></i>Gruntwell</div>
  <p class="copyright">Copyright ©2013 Verlaniinc &nbsp;- All rights reserved</p>
</footer>

</body>
</html>
```